Thriller Book Cover design - Unique!

Hi, I have an already made cover design but i need to take it to the next level.
I want something unique that would attract everyone walking by in a book store.
Maybe 3D look or anything else that is not already used in book cover designs.
TRY to come up with something ORIGINAL. Not just using my existing cover.

The title fonts and bible references should be the same. They are provided in AI.files

Story: The Quillmoor is the most gruesome and terrifying thriller ever. The slogan of the book should also be added and it's "When the unknown strikes"

Thanks

Industry/Entity Type

Store

Requirements
Should not have
• No clichés for thriller books : No blood stains, overused fonts etc....

```html
<!DOCTYPE html>
<html lang="en">
<head>
<meta charset="utf-8">
<title>The Quillmoor — Book Cover</title>
<link rel="stylesheet" href="https://fonts.googleapis.com/css2?family=Rubik+Distressed&family=Montserrat:wght@500;600&display=swap">
<style>
  :root {
    --paper: #f6f1f1;
    --blush: #f0b9b9;
    --rose: #e48d8f;
    --ink: #231617;
    --figure: #1f0f10;
    --author-ink: #1c1a1b;
    --slogan-ink: #3a2224;
  }
  html, body {
    margin: 0;
    padding: 0;
    width: 855px;
    height: 1200px;
    overflow: hidden;
    background: var(--paper);
  }
  .cover {
    position: relative;
    width: 855px;
    height: 1200px;
    overflow: hidden;
    background:
      radial-gradient(ellipse 62% 46% at 50% 42%, var(--rose) 0%, var(--blush) 45%, rgba(240,185,185,0) 80%),
      linear-gradient(180deg, #f3eeee 0%, #f7e7e7 50%, #f1eded 100%);
  }
  .rain-glass {
    position: absolute;
    inset: 0;
    background: radial-gradient(ellipse 70% 60% at 50% 45%, rgba(214,110,115,0.18), rgba(255,255,255,0) 75%);
  }
  .hooded-figure {
    position: absolute;
    left: 150px;
    top: 260px;
    width: 590px;
    height: 740px;
    background: radial-gradient(ellipse 46% 50% at 50% 48%, var(--figure) 0%, rgba(40,18,20,0.9) 55%, rgba(60,25,28,0) 100%);
  }
  .title {
    position: absolute;
    top: 78px;
    left: 0;
    width: 855px;
    margin: 0;
    text-align: center;
    font-family: "Rubik Distressed", "Impact", sans-serif;
    font-weight: 400;
    font-size: 104px;
    line-height: 1;
    letter-spacing: 2px;
    color: var(--ink);
    white-space: nowrap;
  }
  .slogan {
    position: absolute;
    top: 212px;
    left: 0;
    width: 855px;
    margin: 0;
    text-align: center;
    font-family: "Montserrat", "Helvetica Neue", sans-serif;
    font-weight: 500;
    font-size: 22px;
    letter-spacing: 9px;
    text-transform: uppercase;
    color: var(--slogan-ink);
  }
  .author {
    position: absolute;
    top: 1062px;
    left: 0;
    width: 855px;
    margin: 0;
    text-align: center;
    font-family: "Montserrat", "Helvetica Neue", sans-serif;
    font-weight: 600;
    font-size: 68px;
    line-height: 1;
    letter-spacing: 10px;
    color: var(--author-ink);
  }
</style>
</head>
<body>
  <main class="cover">
    <div class="rain-glass" role="img" aria-label="Rain droplets streaming down a misted pink-tinted glass pane"></div>
    <div class="hooded-figure" role="img" aria-label="Dark silhouette of a hooded figure standing behind wet glass"></div>
    <h1 class="title">The Quillmoor</h1>
    <p class="slogan">When the unknown strikes</p>
    <p class="author">R.L. VASHTI</p>
  </main>
</body>
</html>
```